Zielgruppe
Die travlon GmbH bietet professionelle Cloud-Lösungen im Bereich spezialisierter Verwaltungssysteme. Hierbei handelt es sich um Software as a Service (SaaS), die zu 100% von der travlon GmbH betrieben und kontinuierlich weiterentwickelt wird.
Aufgabenstellung
Das Design kann Farben und/oder Elemente der travlon GmbH enthalten (www.travlon.de). Da es sich um ein eigenen Produkt handelt, muss jedoch auch Neutralität bewahrt werden.

```html
<!DOCTYPE html>
<html lang="de">
<head>
<meta charset="utf-8">
<title>Zonaro – Domain Liste</title>
<link href="https://fonts.googleapis.com/css2?family=Roboto:wght@400;500;700&display=swap" rel="stylesheet">
<style>
:root{
  --red:#e31b23;
  --page:#f2f2f2;
  --white:#ffffff;
  --ink:#1f1f1f;
  --muted:#9a9a9a;
  --line:#dcdcdc;
  --green:#1fbf8f;
  --grey-bar:#a3a3a3;
  --tip:#4a4a4a;
}
*{box-sizing:border-box;margin:0;padding:0}
html,body{width:1200px;height:675px;overflow:hidden}
body{background:var(--page);font-family:'Roboto',sans-serif;color:var(--ink);position:relative;font-size:9.4px}
.abs{position:absolute}

/* header */
.topbar{position:absolute;left:0;top:0;width:1200px;height:62.5px;background:var(--red);color:var(--white)}
.brand{position:absolute;left:174px;top:21px;display:flex;align-items:center;gap:7px;font-size:17px;font-weight:500}
.brand-dot{width:18px;height:18px;border:1.6px solid var(--white);border-radius:50%}
.notice{position:absolute;left:610px;display:flex;align-items:center;gap:6px;font-size:8.8px}
.meta{position:absolute;top:14px;font-size:8.8px}
.session{position:absolute;left:941px;top:14px;font-size:8.8px;font-weight:700}
.session-bar{position:absolute;left:941px;top:30.5px;width:84px;height:4px;background:var(--white);border-radius:2px;overflow:hidden}
.session-bar span{display:block;width:60px;height:100%;background:var(--green)}
.session-time{position:absolute;left:941px;top:40px;font-size:7.5px}
.logout{position:absolute;left:1127px;top:26px;display:flex;align-items:center;gap:5px;font-size:8.8px;font-weight:500}

/* main nav */
.mainnav{position:absolute;left:0;top:62.5px;width:1200px;height:34.5px;background:var(--white)}
.mainnav a{position:absolute;top:13px;font-size:8.8px;font-weight:500;color:var(--ink);text-decoration:none}
.mainnav a.active{color:var(--red)}
.mainnav a.active::after{content:"";position:absolute;left:0;right:0;top:20px;height:2px;background:var(--red)}

/* sidebar */
.sidebar{position:absolute;left:175px;top:127.5px;width:197.5px;height:507.5px;background:var(--white);border-radius:3px;box-shadow:0 1px 2px rgba(0,0,0,.06)}
.side-item{position:absolute;left:0;width:197.5px;height:25.6px;padding-left:20px;display:flex;align-items:center;font-size:9.6px;font-weight:500}
.side-item.active{background:var(--red);color:var(--white);border-radius:3px 3px 0 0}
.side-item svg{position:absolute;right:14px}

/* cards */
.card{position:absolute;background:var(--white);border-radius:3px;box-shadow:0 1px 2px rgba(0,0,0,.06);overflow:hidden}
.card-top{position:absolute;left:0;top:0;width:100%;height:6px}
.card-title{position:absolute;left:20px;font-size:12.5px;font-weight:500}
.label{position:absolute;font-size:8.8px;font-weight:500}
.field{position:absolute;height:19px;border:1px solid var(--line);border-radius:3px;background:var(--white);font-size:8.8px;display:flex;align-items:center;padding:0 7px;color:var(--muted)}
.field.focus{border:1.5px solid #f2a2a6;box-shadow:0 0 0 1px #fbe1e2;color:var(--ink)}
.field svg{position:absolute;right:7px}
.btn{position:absolute;height:22px;background:var(--red);color:var(--white);border-radius:3px;font-size:8.8px;font-weight:700;display:flex;align-items:center;justify-content:center}

/* table */
.table{position:absolute;left:20px;top:83px;width:593px;height:127px;border:1px solid var(--line);border-radius:3px;overflow:visible}
.thead{position:absolute;left:0;top:0;width:100%;height:29px;background:#f5f5f5;border-bottom:1px solid var(--line);border-radius:3px 3px 0 0}
.th{position:absolute;top:10px;font-size:8.8px;font-weight:500}
.row{position:absolute;left:0;width:100%;height:30px;border-bottom:1px solid #e8e8e8}
.row:last-child{border-bottom:none}
.check{position:absolute;left:9.5px;top:10px;width:10px;height:10px;border:1px solid #b5b5b5;border-radius:2px;background:var(--white)}
.check.on{background:var(--green);border-color:var(--green)}
.dots{position:absolute;left:29.5px;top:12.5px;display:flex;gap:3px}
.dots i{width:5.5px;height:5.5px;border-radius:50%;border:1px solid #d0d0d0}
.dots i.live{background:var(--green);border-color:var(--green)}
.domain{position:absolute;left:72px;top:9.5px;font-size:8.8px;display:flex;align-items:center;gap:10px}
.badge{border:1px solid var(--green);color:var(--green);border-radius:6px;font-size:5.2px;font-weight:700;padding:0.5px 4px}
.icon{position:absolute;top:6px;width:18px;height:18px;border-radius:50%;display:flex;align-items:center;justify-content:center}
.icon.hover{background:#efefef}
.tip{position:absolute;background:var(--tip);color:var(--white);font-size:7px;border-radius:2px;padding:2px 5px;white-space:nowrap;z-index:2}
</style>
</head>
<body>

<header class="topbar">
  <div class="brand"><span class="brand-dot"></span>Zonaro</div>
  <div class="notice" style="top:14px">
    <svg width="10" height="8" viewBox="0 0 10 8"><rect x="0.5" y="0.5" width="9" height="7" fill="none" stroke="#fff"/><path d="M0.5 0.8 5 4.5 9.5 0.8" fill="none" stroke="#fff"/></svg>
    neue Nachrichten
  </div>
  <div class="notice" style="top:29px">
    <svg width="10" height="10" viewBox="0 0 10 10"><circle cx="5" cy="5" r="5" fill="#fff"/><path d="M5 2.3V5.3H7.2" fill="none" stroke="#e31b23" stroke-width="1.2"/></svg>
    Aufragsstapel
  </div>
  <div class="meta" style="left:816px">Version: 2.2.8</div>
  <div class="meta" style="left:879px">Sitemap</div>
  <div class="session">angemeldet als jonas</div>
  <div class="session-bar"><span></span></div>
  <div class="session-time">120 min. Restzeit</div>
  <div class="logout">
    <svg width="11" height="10" viewBox="0 0 11 10"><path d="M5 1H1V9H5" fill="none" stroke="#fff" stroke-width="1.2"/><path d="M4 5H10M7.5 2.5 10 5 7.5 7.5" fill="none" stroke="#fff" stroke-width="1.2"/></svg>
    Logout
  </div>
</header>

<nav class="mainnav">
  <a style="left:474px">Start</a>
  <a style="left:523px">Benutzer</a>
  <a style="left:588px">Kontakt</a>
  <a class="active" style="left:649px">Domain</a>
  <a style="left:709px">DNS</a>
</nav>

<aside class="sidebar">
  <div class="side-item active" style="top:0">Domain Liste</div>
  <div class="side-item" style="top:30.6px">Domain registrieren</div>
  <div class="side-item" style="top:61.2px">Domain transferieren</div>
  <div class="side-item" style="top:91.8px">Domain bearbeiten</div>
  <div class="side-item" style="top:122.4px">Domain wiederherstellen</div>
  <div class="side-item" style="top:153px">Messenaufrage</div>
  <div class="side-item" style="top:183.6px">DNSSEC<svg width="8" height="5" viewBox="0 0 8 5"><path d="M1 1 4 4 7 1" fill="none" stroke="#1f1f1f" stroke-width="1.2"/></svg></div>
  <div class="side-item" style="top:214.2px">Werkzeug<svg width="8" height="5" viewBox="0 0 8 5"><path d="M1 1 4 4 7 1" fill="none" stroke="#1f1f1f" stroke-width="1.2"/></svg></div>
</aside>

<section class="card" style="left:392.5px;top:127.5px;width:632.5px;height:223.5px">
  <div class="card-top" style="background:var(--red)"></div>
  <div class="card-title" style="top:21px">Listen-Filter</div>
  <div class="label" style="left:398px;top:23.5px">Zeilen pro siete</div>
  <div class="field" style="left:463px;top:20.5px;width:53px;height:14px;font-size:7px">-
    <svg width="7" height="4" viewBox="0 0 7 4"><path d="M0.5 0.5 3.5 3.5 6.5 0.5" fill="none" stroke="#777"/></svg></div>
  <div class="label" style="left:528px;top:23.5px">Wreiter optionen</div>
  <svg class="abs" style="left:600px;top:22px" width="10" height="10" viewBox="0 0 10 10"><path d="M5 1V9M1 5H9" stroke="#999" stroke-width="1"/></svg>

  <div class="label" style="left:20px;top:60.5px">Domain*</div>
  <div class="field focus" style="left:112.5px;top:56px;width:150px;height:21px">zonaro.co|</div>
  <div class="label" style="left:20px;top:90px">Benutzer*</div>
  <div class="field" style="left:112.5px;top:85.5px;width:150px"><svg width="7" height="4" viewBox="0 0 7 4"><path d="M0.5 0.5 3.5 3.5 6.5 0.5" fill="none" stroke="#555"/></svg></div>
  <div class="label" style="left:20px;top:119.5px">Renewal-Mode*</div>
  <div class="field" style="left:112.5px;top:115px;width:150px"><svg width="7" height="4" viewBox="0 0 7 4"><path d="M0.5 0.5 3.5 3.5 6.5 0.5" fill="none" stroke="#555"/></svg></div>
  <div class="label" style="left:20px;top:148.5px">Expire On*</div>
  <div class="field" style="left:112.5px;top:144px;width:150px;font-size:8px">DD/MM/YYYY
    <svg width="9" height="9" viewBox="0 0 9 9"><rect x="0.5" y="1.5" width="8" height="7" fill="none" stroke="#555"/><path d="M0.5 3.5H8.5M2.5 0V2M6.5 0V2" stroke="#555"/><rect x="5" y="5" width="2" height="2" fill="#555"/></svg></div>

  <div class="label" style="left:371px;top:62.5px">Umlautdomain*</div>
  <div class="field" style="left:462.5px;top:58px;width:150px"></div>
  <div class="label" style="left:371px;top:91px">Kontakt*</div>
  <div class="field" style="left:462.5px;top:86.5px;width:150px"></div>
  <div class="label" style="left:371px;top:120px">Lock-Status*</div>
  <div class="field" style="left:462.5px;top:115.5px;width:150px"><svg width="7" height="4" viewBox="0 0 7 4"><path d="M0.5 0.5 3.5 3.5 6.5 0.5" fill="none" stroke="#555"/></svg></div>
  <div class="label" style="left:371px;top:148.5px">bis*</div>
  <div class="field" style="left:462.5px;top:144px;width:150px;font-size:8px">DD/MM/YYYY
    <svg width="9" height="9" viewBox="0 0 9 9"><rect x="0.5" y="1.5" width="8" height="7" fill="none" stroke="#555"/><path d="M0.5 3.5H8.5M2.5 0V2M6.5 0V2" stroke="#555"/><rect x="5" y="5" width="2" height="2" fill="#555"/></svg></div>

  <div class="btn" style="left:502px;top:182px;width:110.5px">Domains auflisten</div>
</section>

<section class="card" style="left:392.5px;top:371px;width:634px;height:264px">
  <div class="card-top" style="background:var(--grey-bar)"></div>
  <div class="card-title" style="top:21px">Liste</div>
  <div class="label" style="right:20px;top:23px">Export CSV</div>
  <div class="label" style="left:20px;top:52px">3 Elemente</div>
  <div class="field" style="left:92px;top:47px;width:250px;color:var(--ink)">neuedesign-zonaro.com - tesdomain-zonaro...
    <svg width="7" height="4" viewBox="0 0 7 4"><path d="M0.5 0.5 3.5 3.5 6.5 0.5" fill="none" stroke="#333" stroke-width="1.1"/></svg></div>

  <div class="table">
    <div class="thead">
      <div class="th" style="left:9.5px">Status</div>
      <div class="th" style="left:72px">Domain</div>
    </div>

    <div class="row" style="top:29px">
      <div class="check on"><svg width="10" height="10" viewBox="0 0 10 10" style="position:absolute;left:-1px;top:-1px"><path d="M2.5 5 4.3 6.8 7.7 3.2" fill="none" stroke="#fff" stroke-width="1.3"/></svg></div>
      <div class="dots"><i></i><i></i><i class="live"></i></div>
      <div class="domain">neuesdesign-zonaro.com <span class="badge">Neu!</span></div>
      <div class="icon hover" style="left:518px"><svg width="11" height="11" viewBox="0 0 11 11"><path d="M5 1.5H1V10H9.5V6" fill="none" stroke="#222" stroke-width="1.1"/><path d="M4 7 4.3 5.2 8.8 0.8 10.2 2.2 5.8 6.7Z" fill="#222"/></svg></div>
      <div class="icon" style="left:543px"><svg width="11" height="11" viewBox="0 0 11 11"><path d="M2 5.5A3.7 3.7 0 1 0 3.2 2.7" fill="none" stroke="#999" stroke-width="1.1"/><path d="M1.2 1.5V4H3.7" fill="none" stroke="#999" stroke-width="1.1"/><path d="M5.7 3.5V5.8L7.2 7" fill="none" stroke="#999" stroke-width="1.1"/></svg></div>
      <div class="icon" style="left:568px"><svg width="4" height="11" viewBox="0 0 4 11"><circle cx="2" cy="1.3" r="1.2" fill="#999"/><path d="M0.5 4H2.6V10M0.5 10H3.5" fill="none" stroke="#999" stroke-width="1.1"/></svg></div>
      <div class="tip" style="left:503px;top:26px">Bearbeiten</div>
    </div>

    <div class="row" style="top:59px">
      <div class="check"></div>
      <div class="dots"><i></i><i></i><i class="live"></i></div>
      <div class="domain">test-zonaro.com <span class="badge">Neu!</span></div>
      <div class="icon" style="left:518px"><svg width="11" height="11" viewBox="0 0 11 11"><path d="M5 1.5H1V10H9.5V6" fill="none" stroke="#999" stroke-width="1.1"/><path d="M4 7 4.3 5.2 8.8 0.8 10.2 2.2 5.8 6.7Z" fill="#999"/></svg></div>
      <div class="icon hover" style="left:543px"><svg width="11" height="11" viewBox="0 0 11 11"><path d="M2 5.5A3.7 3.7 0 1 0 3.2 2.7" fill="none" stroke="#222" stroke-width="1.2"/><path d="M1.2 1.5V4H3.7" fill="none" stroke="#222" stroke-width="1.2"/><path d="M5.7 3.5V5.8L7.2 7" fill="none" stroke="#222" stroke-width="1.2"/></svg></div>
      <div class="icon" style="left:568px"><svg width="4" height="11" viewBox="0 0 4 11"><circle cx="2" cy="1.3" r="1.2" fill="#999"/><path d="M0.5 4H2.6V10M0.5 10H3.5" fill="none" stroke="#999" stroke-width="1.1"/></svg></div>
      <div class="tip" style="left:533px;top:26px">Historie</div>
    </div>

    <div class="row" style="top:89px">
      <div class="check"></div>
      <div class="dots"><i></i><i></i><i class="live"></i></div>
      <div class="domain">testdomain-zonaro.com <span class="badge">Neu!</span></div>
      <div class="icon" style="left:518px"><svg width="11" height="11" viewBox="0 0 11 11"><path d="M5 1.5H1V10H9.5V6" fill="none" stroke="#999" stroke-width="1.1"/><path d="M4 7 4.3 5.2 8.8 0.8 10.2 2.2 5.8 6.7Z" fill="#999"/></svg></div>
      <div class="icon" style="left:543px"><svg width="11" height="11" viewBox="0 0 11 11"><path d="M2 5.5A3.7 3.7 0 1 0 3.2 2.7" fill="none" stroke="#999" stroke-width="1.1"/><path d="M1.2 1.5V4H3.7" fill="none" stroke="#999" stroke-width="1.1"/><path d="M5.7 3.5V5.8L7.2 7" fill="none" stroke="#999" stroke-width="1.1"/></svg></div>
      <div class="icon hover" style="left:568px"><svg width="4" height="11" viewBox="0 0 4 11"><circle cx="2" cy="1.3" r="1.2" fill="#222"/><path d="M0.5 4H2.6V10M0.5 10H3.5" fill="none" stroke="#222" stroke-width="1.3"/></svg></div>
      <div class="tip" style="left:560px;top:26px">Whois</div>
    </div>
  </div>

  <div class="btn" style="left:514.5px;top:222px;width:99.5px">Massenauftrag</div>
</section>

</body>
</html>
```